Swim school needs flyer design

Need revamp of flyer design. Attached last years flyer (BCP A4 Holiday Leaflet-v6.2 (1)). Also attached is this years information in word format (BCP A4 BCP & Holiday Leaflet 2014-2015).
This flyer must fit with our logo (Blue Current Pools-RGB). This flyer is our first point of call for many of our clients. With the amount of information that must be provided, it is important that it flows and is appealing. Photos can be accessed from http://kemapics.brightfolio.net/apps/photos/album?albumid=52930417 or from your own source
Important that the final design fits printers template.(Flyers-A4-210x297mm-2Side - attached)

```html
<!DOCTYPE html>
<html lang="en">
<head>
<meta charset="utf-8">
<title>Blue Current Pools – Flyers</title>
<link href="https://fonts.googleapis.com/css2?family=Source+Sans+3:wght@400;600;700&display=swap" rel="stylesheet">
<style>
:root{
  --blue:#10a8dc;
  --blue-dark:#0a8fc4;
  --blue-light:#7fd3f0;
  --orange:#f7941d;
  --green:#a6c53a;
  --white:#ffffff;
  --ink:#3c3c3c;
  --stage:#2b2b2b;
}
*{margin:0;padding:0;box-sizing:border-box}
html,body{width:1200px;height:1000px;overflow:hidden;background:var(--stage);font-family:"Source Sans 3",Arial,sans-serif}
.flyer{position:absolute;top:92px;width:575px;height:815px;background:var(--white);overflow:hidden}
.flyer--holiday{left:20px}
.flyer--terms{left:614px}
.flyer__bg{position:absolute;inset:0}
.abs{position:absolute}
.title-main{color:var(--orange);font-weight:700;line-height:.9;letter-spacing:-1px}
.title-sub{color:var(--blue);font-weight:700;line-height:1}
.photo{position:absolute;border-radius:50%;border:5px solid var(--white)}
.photo--pool{background:radial-gradient(circle at 40% 40%,#9fdcf2,#2e9fcf 70%,#1b7fb0)}
.lead{font-size:19px;font-weight:700;line-height:1.12;color:var(--white)}
.note{font-size:10.5px;color:#e6f6fc;line-height:1.35}
.h-important{font-size:19px;font-weight:700;color:var(--white);letter-spacing:.5px}
.bullets{list-style:none;font-size:9.5px;color:var(--white);line-height:1.5}
.bullets li::before{content:"• "}
.contact h3{font-size:15px;font-weight:700;color:var(--white);line-height:1.15;margin-top:10px}
.contact p{font-size:10.5px;color:var(--white);line-height:1.4}
.dates{position:absolute;left:340px;top:192px;width:222px}
.dates__head{background:var(--orange);color:var(--white);font-weight:700;font-size:13.5px;padding:2px 6px;height:22px}
.dates__body{display:flex;border:2px solid var(--blue);background:var(--blue)}
.dates__years{width:72px;display:flex;flex-direction:column;color:var(--white);font-weight:700;font-size:19px}
.dates__years span{flex:1;display:flex;align-items:center;justify-content:center}
.dates__rows{flex:1}
.dates__rows div{height:18.6px;font-size:12px;padding-left:5px;line-height:18px;border-bottom:1px solid var(--blue);background:var(--white);color:var(--ink)}
.dates__rows div.alt{background:var(--blue);color:var(--ink)}
.dates__foot{font-size:12px;color:var(--ink);margin-top:5px}
.footer{position:absolute;left:0;right:0;bottom:0;height:85px}
.brand{position:absolute;left:34px;top:26px;display:flex;align-items:center;gap:7px}
.brand__dot{width:14px;height:14px;border-radius:50%;background:var(--orange)}
.brand__name{font-size:19px;font-weight:700;color:var(--blue)}
.footer__rule{position:absolute;top:18px;width:1px;height:52px;background:#bbb}
.footer__web{position:absolute;left:231px;top:20px;font-size:10.5px;color:var(--ink)}
.footer__phone{position:absolute;left:231px;top:34px;font-size:27px;font-weight:700;color:var(--orange)}
.footer__addr{position:absolute;left:413px;top:18px;font-size:10.5px;color:#555;line-height:1.35}
.term{position:absolute;left:40px;width:210px;color:var(--white)}
.term h4{font-size:13px;font-weight:700;text-align:center;line-height:1.2}
.term p{font-size:10.5px;color:#e6f6fc;margin:1px 0 3px}
.prices{border-collapse:collapse;width:208px;font-size:11.5px}
.prices td{border:1.5px solid var(--white);padding:1px 4px;height:19px}
.pathway{position:absolute;left:320px;top:203px}
.pathway h2{font-size:19px;font-weight:700;color:var(--blue);line-height:1.1;letter-spacing:.3px}
.pathway h5{font-size:15.5px;font-weight:700;color:var(--orange);margin-top:6px;line-height:1.1}
.pathway p{font-size:15.5px;color:var(--ink);line-height:1.15}
.terms-important{position:absolute;left:270px;top:455px;width:280px}
.terms-important .bullets{font-size:8.6px;line-height:1.38}
.terms-important .bullets li{font-weight:600}
.closing{font-size:9.5px;font-weight:700;color:var(--white);line-height:1.6}
</style>
</head>
<body>

<section class="flyer flyer--holiday">
  <svg class="flyer__bg" viewBox="0 0 575 815" width="575" height="815" aria-hidden="true">
    <path d="M0 118 C130 112 250 148 380 146 C470 145 530 128 575 110 L575 150 C500 170 420 180 330 178 C200 176 100 145 0 135Z" fill="var(--green)"/>
    <path d="M395 165 C450 160 500 150 560 130" stroke="var(--blue-light)" stroke-width="7" fill="none" stroke-linecap="round"/>
    <circle cx="350" cy="36" r="9" fill="var(--orange)"/>
    <circle cx="372" cy="26" r="9" fill="none" stroke="var(--orange)" stroke-width="1.5"/>
    <circle cx="355" cy="62" r="16" fill="var(--green)"/>
    <circle cx="386" cy="50" r="11" fill="none" stroke="var(--green)" stroke-width="1.5"/>
    <path d="M0 300 C120 300 230 320 290 375 C330 410 380 422 575 412 L575 730 C380 750 200 740 0 760Z" fill="var(--blue)"/>
    <path d="M282 368 C322 405 372 420 575 406" stroke="var(--blue-light)" stroke-width="12" fill="none" opacity=".75"/>
    <circle cx="211" cy="197" r="8" fill="var(--blue)" opacity=".6"/>
    <circle cx="224" cy="214" r="6" fill="var(--blue)" opacity=".8"/>
    <circle cx="224" cy="232" r="10" fill="var(--blue)"/>
    <path d="M0 722 C200 702 380 707 575 682 L575 727 C380 747 200 742 0 757Z" fill="var(--green)"/>
    <path d="M0 752 C200 732 380 737 575 717 L575 815 L0 815Z" fill="var(--white)"/>
    <line x1="302" y1="438" x2="302" y2="705" stroke="var(--white)" stroke-dasharray="2 3"/>
    <line x1="40" y1="484" x2="290" y2="484" stroke="var(--white)" stroke-dasharray="2 3"/>
    <line x1="40" y1="618" x2="290" y2="618" stroke="var(--white)" stroke-dasharray="2 3"/>
  </svg>

  <div class="abs" style="left:38px;top:26px">
    <div class="title-main" style="font-size:56px">HOLIDAY</div>
    <div class="title-sub" style="font-size:31px">SWIM CLASSES</div>
  </div>

  <div class="photo photo--pool" role="img" aria-label="Photo of a child in goggles and swim cap in the pool" style="left:20px;top:160px;width:168px;height:168px"></div>
  <div class="photo photo--pool" role="img" aria-label="Photo of a baby swimming underwater" style="left:196px;top:230px;width:112px;height:112px"></div>

  <div class="dates">
    <div class="dates__head">HOLIDAY PROGRAM DATES</div>
    <div class="dates__body">
      <div class="dates__years"><span>2014</span><span>2015</span></div>
      <div class="dates__rows">
        <div class="alt">Sep 23rd – 27th</div>
        <div>Sep 30th – Oct 4th</div>
        <div class="alt">Jan 6th – 10th</div>
        <div>Jan 13th – 17th</div>
        <div class="alt">Jan 20th – 24th</div>
        <div>Mar 30th – Apr 3rd</div>
        <div class="alt">Apr 6th – 10th</div>
        <div>Jun 29th – Jul 3rd</div>
      </div>
    </div>
    <div class="dates__foot">* $52 per child due to 4 day week</div>
  </div>

  <div class="abs lead" style="left:40px;top:342px">
    Salt Water Pool<br>Ages 3 and older<br>$75 per child per week<br>(5x½ hour classes per week)
  </div>
  <div class="abs note" style="left:40px;top:433px;width:260px">
    No bookings are taken without a fully completed enrolment form and payment.<br>
    Places are limited so book early to avoid disappointment.
  </div>

  <div class="abs" style="left:40px;top:492px;width:260px">
    <div class="h-important">IMPORTANT</div>
    <ul class="bullets">
      <li>All holiday swim classes are conducted at the Westbrook primary school pool</li>
      <li>30 minute classes run every ½ hour from 9.30am to 12 noon</li>
      <li>Limited places due to small class sizes</li>
      <li>Beginners to advanced swimmers welcome</li>
      <li>All children are grouped by age and ability</li>
      <li>No refunds or makeups for holiday programs</li>
    </ul>
  </div>
  <div class="abs" style="left:40px;top:626px;width:260px;font-size:11px;font-weight:700;color:var(--white);line-height:1.3">
    Our qualified staff makes Blue Current Pools not only a rewarding but also a lot of fun.<br>
    This is a great opportunity to kick-start your child's aquatic education.
  </div>

  <div class="abs contact" style="left:320px;top:440px;width:240px">
    <h3 style="font-size:15.5px;margin-top:0">Pool Locations<br>Contact Details &amp; Office Hours</h3>
    <h3>Westbrook P.S. Pool</h3>
    <p>Location: 42 Harbour Lane, Westbrook 3088<br>Phone: 9000 4821<br>Office Hours: Mon-Fri 9:00am-5.30pm,<br><span style="padding-left:74px">Sat-Sun 9.15am-12.15pm</span></p>
    <h3>Ridgeway College Pool</h3>
    <p>Location: Gate 3, Elm Street,<br>Ridgeway 3071</p>
    <h3>All Correspondence</h3>
    <p>Post: P.O. Box 1180, North Ridgeway 3071<br>Email: info@bluecurrentpools.com.au<br>ABN: 12 345 678 901</p>
  </div>

  <footer class="footer">
    <div class="brand"><span class="brand__dot"></span><span class="brand__name">Blue Current Pools</span></div>
    <span class="footer__rule" style="left:212px"></span>
    <div class="footer__web">www.bluecurrentpools.com.au</div>
    <div class="footer__phone">9000 4821</div>
    <span class="footer__rule" style="left:394px"></span>
    <div class="footer__addr">Westbrook P.S. Pool<br>42 Harbour Lane Westbrook<br>Ridgeway College Pool<br>Gate 3, Elm St Ridgeway</div>
  </footer>
</section>

<section class="flyer flyer--terms">
  <svg class="flyer__bg" viewBox="0 0 575 815" width="575" height="815" aria-hidden="true">
    <path d="M0 112 C130 106 250 140 380 138 C470 137 530 120 575 104 L575 145 C500 162 420 172 330 170 C200 168 100 138 0 128Z" fill="var(--green)"/>
    <path d="M395 158 C450 152 500 142 560 122" stroke="var(--blue-light)" stroke-width="7" fill="none" stroke-linecap="round"/>
    <circle cx="263" cy="123" r="7" fill="none" stroke="var(--green)" stroke-width="1.3"/>
    <circle cx="268" cy="128" r="8" fill="var(--green)"/>
    <path d="M0 290 C90 270 200 255 270 240 C300 232 310 230 320 240 C290 300 285 360 300 420 C330 460 440 450 575 430 L575 730 C380 750 200 740 0 760Z" fill="var(--blue)"/>
    <path d="M320 240 C290 300 285 370 310 420" stroke="var(--blue-light)" stroke-width="12" fill="none" opacity=".7"/>
    <circle cx="295" cy="203" r="5" fill="var(--blue)"/>
    <circle cx="298" cy="218" r="6" fill="var(--blue)" opacity=".7"/>
    <circle cx="205" cy="243" r="13" fill="var(--blue-light)" opacity=".8"/>
    <circle cx="235" cy="272" r="17" fill="var(--blue-light)"/>
    <path d="M0 715 C200 690 380 700 575 680 L575 722 C380 745 200 737 0 752Z" fill="var(--green)"/>
    <path d="M0 747 C200 727 380 735 575 715 L575 815 L0 815Z" fill="var(--white)"/>
    <line x1="246" y1="427" x2="246" y2="700" stroke="var(--white)" stroke-dasharray="2 3"/>
    <line x1="246" y1="640" x2="548" y2="640" stroke="var(--white)" stroke-dasharray="2 3"/>
  </svg>

  <div class="abs" style="left:38px;top:28px">
    <div class="title-main" style="font-size:42px">BLUE CURRENT</div>
    <div class="title-sub" style="font-size:34px">POOLS CLASSES</div>
    <div style="font-size:13px;font-weight:700;color:#555;margin-top:3px">2014/15 Term Dates &amp; Prices</div>
  </div>

  <div class="photo photo--pool" role="img" aria-label="Photo of an instructor holding a baby in the pool" style="left:30px;top:158px;width:136px;height:136px"></div>

  <div class="pathway">
    <h2>OUR STREAMLINED<br>PATHWAY TO SUCCESS</h2>
    <h5>Baby Awareness</h5><p>½ hour class per week</p>
    <h5>Baby Transition Classes</h5><p>½ hour class per week</p>
    <h5>Blue Current Pools Classes</h5><p>½ hour class per week</p>
    <h5>Transitional Stroke Group</h5><p>1 hour class per week</p>
  </div>

  <div class="term" style="top:302px">
    <h4>*2014: Term 4 – 10 week term<br>Oct 6th – Dec 14th</h4>
    <p>Bookings taken from 22nd Sep 2014</p>
    <table class="prices"><tr><td>Babies</td><td>Transition</td><td>BCP</td><td>TSG</td></tr><tr><td>$155</td><td>$165</td><td>$170</td><td>$210</td></tr></table>
  </div>
  <div class="term" style="top:400px">
    <h4>*2015: Term 1 – 9 week term<br>Jan 27th – Mar 29th</h4>
    <p>Bookings taken from 15th Dec 2014</p>
    <table class="prices"><tr><td>Babies</td><td>Transition</td><td>BCP</td><td>TSG</td></tr><tr><td>$139.5</td><td>$148.5</td><td>$153</td><td>$189</td></tr></table>
  </div>
  <div class="term" style="top:498px">
    <h4>*2015: Term 2 – 11 week term<br>Apr 13th – Jun 28th</h4>
    <p>Bookings taken from 30th Mar 2015</p>
    <table class="prices"><tr><td>Babies</td><td>Transition</td><td>BCP</td><td>TSG</td></tr><tr><td>$170.5</td><td>$176</td><td>$181.5</td><td>$189</td></tr></table>
  </div>
  <div class="term" style="top:596px">
    <h4>*2015: Term 3 – 10 week term<br>Jul 13th – Sep 20th</h4>
    <p>Bookings taken from 29th Jun 2015</p>
    <table class="prices"><tr><td>Babies</td><td>Transition</td><td>BCP</td><td>TSG</td></tr><tr><td>$160</td><td>$170</td><td>$175</td><td>$215</td></tr></table>
  </div>

  <div class="terms-important">
    <div class="h-important">IMPORTANT</div>
    <ul class="bullets">
      <li>No bookings are taken without a fully completed enrolment form and payment.</li>
      <li>Read BCP Policies and Procedures for information on discounts, payment methods, refunds and makeups.</li>
      <li>Book early – place are limited due to small class sizes.</li>
      <li>Bookings can only be made in person at our Westbrook Office or online.</li>
      <li>During holidays, all bookings must be done via the Westbrook Office.</li>
      <li>Photographs and video footage is not allowed to be taken without the permission of all the parents/ guardians whose children are in the class.</li>
      <li>Note that these terms have public holidays and prices will be adjusted accordingly.</li>
    </ul>
    <p class="closing" style="margin-top:16px">All swimmers, male and female, are required to wear a cap<br>please name your cap and goggles with a biro to prevent it washing off.</p>
  </div>

  <footer class="footer">
    <div class="brand"><span class="brand__dot"></span><span class="brand__name">Blue Current Pools</span></div>
    <span class="footer__rule" style="left:212px"></span>
    <div class="footer__web">www.bluecurrentpools.com.au</div>
    <div class="footer__phone">9000 4821</div>
    <span class="footer__rule" style="left:394px"></span>
    <div class="footer__addr">Westbrook P.S. Pool<br>42 Harbour Lane Westbrook<br>Ridgeway College Pool<br>Gate 3, Elm St Ridgeway</div>
  </footer>
</section>

</body>
</html>
```